Animal Eye Clinic needs a Business card

We are a new veterinary ophthalmology practice (Tessaly Animal Eye Care) and we need a business card designed. We only see animal eyes - we are not a regular veterinary clinic. We already have a logo. We are looking for a professional, good looking business card to hand out to our clients. We are looking for something simple but professional and contemporary. Our logo is likely the only picture/graphic that needs to be on the card.
Updates

Contact Information for Business Card

Marisol Dunkley, BSc, DVM, MSc, DipACVO
Veterinary Ophthalmologist

Phone: 250.418.3097
Email: tessalyanimaleyecare@mailbrook.net
Website: tessalyanimaleyecare.net
Address: 1840 Pellworth Rd
Kelowna, BC, V4T 8M3

Colors

Designer to choose colors to be used in the design.

Requirements
Must have
• Our logo (attached)

```html
<!DOCTYPE html>
<html lang="en">
<head>
<meta charset="utf-8">
<title>Tessaly Animal Eye Care — Business Card</title>
<link href="https://fonts.googleapis.com/css2?family=Questrial&family=Open+Sans:wght@400&display=swap" rel="stylesheet">
<style>
  :root {
    --bg: #e9e6e2;
    --card: #050505;
    --teal: #0f9bb0;
    --faint: #161616;
  }
  html, body {
    margin: 0;
    padding: 0;
    width: 1200px;
    height: 900px;
    overflow: hidden;
    background: var(--bg);
  }
  .canvas {
    position: relative;
    width: 1200px;
    height: 900px;
  }
  .card {
    position: absolute;
    left: 250px;
    width: 700px;
    height: 400px;
    background: var(--card);
    overflow: hidden;
    box-shadow: 0 6px 18px rgba(0,0,0,0.18);
  }
  .card--front { top: 30px; }
  .card--back { top: 470px; }

  .brand {
    display: flex;
    align-items: center;
    gap: 12px;
  }
  .brand__dot {
    border-radius: 50%;
    background: var(--teal);
    flex: none;
  }
  .brand__name {
    font-family: "Questrial", sans-serif;
    color: var(--teal);
    white-space: nowrap;
  }

  .card--front .brand {
    position: absolute;
    left: 40px;
    top: 44px;
  }
  .card--front .brand__dot { width: 30px; height: 30px; }
  .card--front .brand__name { font-size: 22px; }

  .front__mark {
    position: absolute;
    right: 40px;
    top: -30px;
    width: 250px;
    height: 250px;
    border-radius: 50%;
    background: var(--faint);
  }

  .person {
    position: absolute;
    left: 40px;
    top: 160px;
    font-family: "Questrial", sans-serif;
    color: var(--teal);
  }
  .person__name {
    font-size: 46px;
    line-height: 1;
    margin: 0 0 12px;
    font-weight: 400;
  }
  .person__credentials {
    font-size: 22px;
    margin: 0 0 4px 60px;
  }
  .person__title {
    font-size: 17px;
    margin: 0 0 0 90px;
  }

  .divider {
    position: absolute;
    left: 440px;
    top: 150px;
    width: 2px;
    height: 190px;
    background: var(--teal);
  }

  .contact {
    position: absolute;
    left: 454px;
    top: 158px;
    margin: 0;
    padding: 0;
    list-style: none;
    font-family: "Open Sans", sans-serif;
    font-size: 10.5px;
    color: var(--teal);
  }
  .contact__item {
    display: flex;
    align-items: center;
    gap: 10px;
    height: 40px;
  }
  .contact__icon {
    width: 20px;
    height: 20px;
    flex: none;
    fill: var(--teal);
  }
  .contact__text { line-height: 1.35; }

  .front__band {
    position: absolute;
    left: 150px;
    right: 56px;
    bottom: 0;
    height: 24px;
    background: var(--teal);
    border-radius: 14px 14px 0 0;
  }

  .card--back .brand {
    position: absolute;
    left: 50%;
    top: 140px;
    transform: translateX(-50%);
    gap: 18px;
  }
  .card--back .brand__dot { width: 60px; height: 60px; }
  .card--back .brand__name { font-size: 34px; }

  .back__web {
    position: absolute;
    left: 0;
    right: 0;
    bottom: 40px;
    text-align: center;
    font-family: "Questrial", sans-serif;
    font-size: 26px;
    color: var(--teal);
    letter-spacing: 0.5px;
  }
</style>
</head>
<body>
<div class="canvas">

  <section class="card card--front" aria-label="Business card front">
    <div class="front__mark" aria-hidden="true"></div>

    <div class="brand">
      <span class="brand__dot" aria-hidden="true"></span>
      <span class="brand__name">Tessaly Animal Eye Care</span>
    </div>

    <div class="person">
      <h1 class="person__name">Marisol Dunkley</h1>
      <p class="person__credentials">BSc, DVM, MSc, DipACVO</p>
      <p class="person__title">Veterinary Ophthalmologist</p>
    </div>

    <div class="divider" aria-hidden="true"></div>

    <ul class="contact">
      <li class="contact__item">
        <svg class="contact__icon" viewBox="0 0 24 24" aria-hidden="true"><path d="M6.6 10.8a15.1 15.1 0 0 0 6.6 6.6l2.2-2.2c.3-.3.7-.4 1-.2 1.1.4 2.3.6 3.6.6.6 0 1 .4 1 1V20c0 .6-.4 1-1 1A17 17 0 0 1 3 4c0-.6.4-1 1-1h3.5c.6 0 1 .4 1 1 0 1.3.2 2.5.6 3.6.1.3 0 .7-.2 1z"/></svg>
        <span class="contact__text">250 - 418 - 3097</span>
      </li>
      <li class="contact__item">
        <svg class="contact__icon" viewBox="0 0 24 24" aria-hidden="true"><path d="M12 2a7 7 0 0 0-7 7c0 5.2 7 13 7 13s7-7.8 7-13a7 7 0 0 0-7-7zm0 9.5A2.5 2.5 0 1 1 12 6.5a2.5 2.5 0 0 1 0 5z"/></svg>
        <span class="contact__text">1840 Pellworth Rd<br>Kelowna, BC, V4T 8M3</span>
      </li>
      <li class="contact__item">
        <svg class="contact__icon" viewBox="0 0 24 24" aria-hidden="true"><path d="M3 5h18v14H3z" fill="none"/><path d="M2 5.5C2 4.7 2.7 4 3.5 4h17c.8 0 1.5.7 1.5 1.5v.3l-10 6.3L2 5.8zM2 8.2l10 6.3 10-6.3v10.3c0 .8-.7 1.5-1.5 1.5h-17c-.8 0-1.5-.7-1.5-1.5z"/></svg>
        <span class="contact__text">tessalyanimaleyecare@mailbrook.net</span>
      </li>
      <li class="contact__item">
        <svg class="contact__icon" viewBox="0 0 24 24" aria-hidden="true"><path d="M5 3l14 8-6 1.6 4 6.4-2.6 1.6-4-6.4L6 18z"/></svg>
        <span class="contact__text">tessalyanimaleyecare.net</span>
      </li>
    </ul>

    <div class="front__band" aria-hidden="true"></div>
  </section>

  <section class="card card--back" aria-label="Business card back">
    <div class="brand">
      <span class="brand__dot" aria-hidden="true"></span>
      <span class="brand__name">Tessaly Animal Eye Care</span>
    </div>
    <p class="back__web">tessalyanimaleyecare.net</p>
  </section>

</div>
</body>
</html>
```